Capital Management company needs a web design

We have a domain name and logo but need hosting and design. Please look at the Must-Haves section.

Target Market(s)

banking industry and investors

Industry/Entity Type

Investment

Coding

Coded - Design and coding required

Number of Pages Required

1 page

Font styles to use
Sans Serif

Requirements
Must have
• Picture(s) of skyscraper skyline (can be of Manhattan, Chicago, or any other major city in the USA).
• Please use the three colors of the logo as a backdrop to part of the webpage(s)
Should not have
• No "what our clients say" section
• No pictures of people

```html
<!DOCTYPE html>
<html lang="en">
<head>
<meta charset="utf-8">
<title>Lakeside Crest Capital</title>
<link href="https://fonts.googleapis.com/css2?family=Josefin+Sans:wght@400;600&display=swap" rel="stylesheet">
<style>
:root{
  --brand-blue:#1a75bb;
  --brand-grey:#9a9a9a;
  --ink:#333333;
  --text:#2a2a2a;
  --white:#ffffff;
  --footer:#313131;
  --sky-top:#4a6fa3;
  --sky-bottom:#3a5487;
  --card-border:#6f6f6f;
}
*{margin:0;padding:0;box-sizing:border-box}
html,body{width:738px;height:1200px;overflow:hidden}
body{position:relative;background:var(--white);font-family:"Josefin Sans",sans-serif;color:var(--text)}
.brand{position:absolute;left:49px;top:10px;display:flex;align-items:center;gap:8px}
.brand-mark{width:14px;height:14px;background:var(--brand-blue)}
.brand-name{font-size:20px;font-weight:600;color:var(--brand-blue);letter-spacing:.5px}
.social{position:absolute;right:50px;top:7px;display:flex;gap:4px}
.social span{width:21px;height:21px;border-radius:50%;background:var(--brand-blue)}
.main-nav{position:absolute;right:50px;top:59px;display:flex;gap:11px;font-size:11px;letter-spacing:.6px;color:var(--ink)}
.hero{position:absolute;left:0;top:103px;width:738px;height:308px;
  background:linear-gradient(180deg,#3f66a0 0%,#6b8bbd 35%,#3a4f8c 62%,#2e3f72 78%,#4d6fa0 100%)}
.service{position:absolute;width:160px;text-align:center}
.service svg{display:block;margin:0 auto}
.service h3{font-weight:400;font-size:15px;margin-top:6px;color:var(--ink);letter-spacing:.4px}
.service p{font-size:10.5px;line-height:22px;margin-top:4px;letter-spacing:.4px}
.btn{display:inline-block;background:var(--brand-blue);color:var(--white);font-size:11px;font-weight:600;
  width:81px;height:25px;line-height:27px;border-radius:3px;text-align:center;letter-spacing:.3px}
.service .btn{margin-top:6px}
.band{position:absolute;left:0;top:645px;width:738px;height:309px;
  background:linear-gradient(180deg,#1e7fc4 0%,#5b9fd4 45%,#b9d6ee 80%,#ffffff 100%)}
.card{position:absolute;background:var(--white);border:1px solid var(--card-border);border-radius:5px;text-align:center;padding-top:22px}
.card h2{font-size:11px;font-weight:400;color:var(--brand-blue);letter-spacing:.6px}
.card p{font-size:10px;line-height:22px;margin:8px auto 0;width:250px;letter-spacing:.4px}
.card .btn{margin-top:10px}
.site-footer{position:absolute;left:0;top:954px;width:738px;height:246px;background:var(--footer);color:var(--white)}
.foot-col{position:absolute;top:82px}
.foot-col h4{font-size:11px;font-weight:600;letter-spacing:.6px;padding-bottom:8px;border-bottom:1.5px solid var(--white);display:inline-block;padding-right:12px}
.foot-col ul{list-style:none;margin-top:11px}
.foot-col li{font-size:9.5px;line-height:22px;letter-spacing:.6px;padding-left:2px}
</style>
</head>
<body>
<header>
  <div class="brand"><span class="brand-mark"></span><span class="brand-name">Lakeside Crest Capital</span></div>
  <div class="social" aria-label="Social links"><span></span><span></span><span></span><span></span></div>
  <nav class="main-nav"><span>ABOUT US</span><span>NEWS ROOM</span><span>INVESIGATOR RELATIONS</span><span>RESPONSIBILITY</span></nav>
</header>

<div class="hero" role="img" aria-label="Photograph of a city skyscraper skyline over the lake under a blue sky"></div>

<section class="services">
  <div class="service" style="left:39px;top:430px">
    <svg width="46" height="45" viewBox="0 0 46 45"><path d="M16 2h14l-4 7h-6z" fill="var(--brand-blue)"/><rect x="17" y="9" width="12" height="3" rx="1" fill="var(--brand-blue)"/><path d="M17 13h12c10 6 15 14 15 21 0 7-5 10-21 10S2 41 2 34c0-7 5-15 15-21z" fill="var(--brand-blue)"/><text x="23" y="36" text-anchor="middle" font-size="17" font-weight="600" fill="#fff" font-family="Josefin Sans,sans-serif">$</text></svg>
    <h3>Asset management</h3>
    <p>Lorem ipsum dolor sit amet, consectetur adipiscing elit, sed do</p>
    <span class="btn">Know More</span>
  </div>
  <div class="service" style="left:280px;top:430px">
    <svg width="46" height="46" viewBox="0 0 46 46"><ellipse cx="22" cy="25" rx="19" ry="14" fill="var(--brand-blue)"/><circle cx="35" cy="8" r="5" fill="var(--brand-blue)"/><rect x="8" y="34" width="6" height="11" rx="2" fill="var(--brand-blue)"/><rect x="27" y="34" width="6" height="11" rx="2" fill="var(--brand-blue)"/><rect x="40" y="22" width="6" height="7" rx="2" fill="var(--brand-blue)"/></svg>
    <h3>Bank</h3>
    <p>Lorem ipsum dolor sit amet, consectetur adipiscing elit, sed do</p>
    <span class="btn">Know More</span>
  </div>
  <div class="service" style="left:548px;top:432px">
    <svg width="42" height="42" viewBox="0 0 42 42"><path d="M3 8l30-5v6z" fill="var(--brand-blue)"/><rect x="2" y="8" width="38" height="32" rx="3" fill="var(--brand-blue)"/><circle cx="33" cy="24" r="2.5" fill="#fff"/></svg>
    <h3>Brookers</h3>
    <p>Lorem ipsum dolor sit amet, consectetur adipiscing elit, sed do</p>
    <span class="btn">Know More</span>
  </div>
</section>

<section class="band">
  <article class="card" style="left:49px;top:33px;width:292px;height:249px">
    <h2>INDIVIDUAL SOLUTION FOR EVERYONE</h2>
    <p>Lorem ipsum dolor sit amet, consectetur adipiscing elit, sed do eiusmod tempor incididunt ut labore et dolore magna aliqua. Quis ipsum suspendisse ultrices gravida. Risus commodo viverra maecenas accumsan lacus vel facilisis.</p>
    <span class="btn">Know More</span>
  </article>
  <article class="card" style="left:399px;top:35px;width:288px;height:247px;padding-top:19px">
    <h2>SIMPLYFI COMPLEX WORLD</h2>
    <p>Lorem ipsum dolor sit amet, consectetur adipiscing elit, sed do eiusmod tempor incididunt ut labore et dolore magna aliqua. Quis ipsum suspendisse ultrices gravida. Risus commodo viverra maecenas accumsan lacus vel facilisis.</p>
    <span class="btn">Know More</span>
  </article>
</section>

<footer class="site-footer">
  <div class="foot-col" style="left:50px"><h4>ABOUT US</h4><ul><li>OVERVIEW</li><li>MISSION AND PRINCIPLE</li><li>LEADERSHIP</li><li>HISTORY</li></ul></div>
  <div class="foot-col" style="left:248px;top:80px"><h4>NEWS ROOM</h4><ul><li>OVERVIEW</li><li>CURRENT NEWS</li></ul></div>
  <div class="foot-col" style="left:373px;top:79px"><h4>INVESTOR RELATION</h4><ul><li>ANNUAL REPORT</li><li>STOCK INFORMATION</li><li>DIVIDENT HISTORY</li></ul></div>
  <div class="foot-col" style="left:561px;top:79px"><h4>RESPONSIBILITY</h4><ul><li>OVERVIEW</li><li>ETHICS AND INTEGRITY</li><li>HEALTH &amp; SAFETY</li><li>SOCIAL IMPACT</li></ul></div>
</footer>
</body>
</html>
```